Investment company needing business card

We are wanting a business card which looks sharp and easy on the eye. We are thinking of having a business card with the logo embossed on it, to really make it stand out. We will only have a small amount of information of the business card, person's name, position, email address and phone number

Danielle Hartig
Executive Assistant
+64 21 574 3162
danielleh@quarvendale.co.nz

Requirements
Must have
• Embossed logo
Should not have
• Not to be busy

```html
<!DOCTYPE html>
<html lang="en">
<head>
<meta charset="utf-8">
<title>Quarvendale Group – Business Card</title>
<link href="https://fonts.googleapis.com/css2?family=Lato:wght@400;900&display=swap" rel="stylesheet">
<style>
  :root {
    --green: #1fae6a;
    --ink: #4a4a4a;
    --grey: #5c5c5c;
    --card: #ffffff;
    --pattern: #f1f1f1;
    --stage: #e6e7e8;
  }
  * { margin: 0; padding: 0; box-sizing: border-box; }
  html, body { width: 1200px; height: 1108px; overflow: hidden; }
  body {
    background: var(--stage);
    font-family: "Lato", sans-serif;
    display: flex;
    flex-direction: column;
    align-items: center;
    justify-content: center;
    gap: 48px;
  }
  .card {
    width: 840px;
    height: 480px;
    background: var(--card);
    box-shadow: 0 6px 18px rgba(0,0,0,.12);
    position: relative;
    overflow: hidden;
  }
  /* Front */
  .card-front { display: flex; align-items: center; padding: 0 64px; }
  .contact { flex: 0 0 360px; }
  .contact-name {
    color: var(--green);
    font-weight: 900;
    font-size: 30px;
    letter-spacing: 1.5px;
    text-transform: uppercase;
  }
  .contact-role { color: var(--ink); font-size: 22px; margin-top: 2px; }
  .contact-list { list-style: none; margin-top: 18px; }
  .contact-list li {
    display: flex; align-items: center; gap: 10px;
    color: var(--ink); font-size: 20px; line-height: 1.6;
  }
  .contact-list svg { width: 16px; height: 16px; fill: var(--green); flex: none; }
  .brand {
    flex: 1;
    display: flex; flex-direction: column; align-items: flex-end;
  }
  .brand-row { display: flex; align-items: center; gap: 14px; }
  .brand-square { width: 34px; height: 34px; background: var(--green); }
  .brand-name {
    color: var(--green);
    font-weight: 900;
    font-size: 34px;
    letter-spacing: 2px;
    text-transform: uppercase;
  }
  .brand-rule { width: 330px; height: 2px; background: var(--grey); margin-top: 14px; }
  /* Back */
  .card-back .pattern-field {
    position: absolute; inset: 0;
    background: var(--pattern);
  }
  .card-back .back-brand {
    position: absolute; right: 250px; top: 50%;
    transform: translateY(-50%);
    display: flex; align-items: center; gap: 10px;
  }
  .card-back .brand-square { width: 22px; height: 22px; }
  .card-back .brand-name { font-size: 22px; letter-spacing: 1.5px; }
</style>
</head>
<body>
  <section class="card card-front">
    <div class="contact">
      <p class="contact-name">Danielle Hartig</p>
      <p class="contact-role">Executive Assistant</p>
      <ul class="contact-list">
        <li>
          <svg viewBox="0 0 16 16"><path d="M3 1h3l1.5 4-2 1.3a9 9 0 0 0 4.2 4.2L11 8.5l4 1.5v3a2 2 0 0 1-2 2A13 13 0 0 1 1 3a2 2 0 0 1 2-2z"/></svg>
          +64 21 574 3162
        </li>
        <li>
          <svg viewBox="0 0 16 16"><path d="M1 3h14v10H1z M2 4.2v.3l6 4.3 6-4.3v-.3z" fill-rule="evenodd"/></svg>
          danielleh@quarvendale.co.nz
        </li>
      </ul>
    </div>
    <div class="brand">
      <div class="brand-row">
        <span class="brand-square"></span>
        <span class="brand-name">Quarvendale Group</span>
      </div>
      <span class="brand-rule"></span>
    </div>
  </section>

  <section class="card card-back">
    <div class="pattern-field" role="img" aria-label="Faint repeating brand-mark pattern across the card back"></div>
    <div class="back-brand">
      <span class="brand-square"></span>
      <span class="brand-name">Quarvendale</span>
    </div>
  </section>
</body>
</html>
```